Upsell Vertical Banner Ad Design For B2B Marketing Agency Vertical 768px × 1180px IS THE SIZE

I need a banner made for my website www.brightlanepromotionhub.biz This banner will be an upsell advertisement for after someone signs up for my monthly program. When they login to their account for the 1st time I will give them the chance to upgrade their account to our annual program with just one click.

this is a page that upsells it currently to give you an idea how we market ourselves:
https://tlpx.pagevault-example.com/page/tlp-annual-upsell

Use this content:

Are You Ready To Commit To Taking Your Business To The Next Level?

Because We're In This For The Long-Haul and Dedicated To Your Success...

Save $300 By Upgrading To An Annual Membership And Pay Only $74/mth

((BUTTON))Yes, Upgrade My Plan Right Now!

*Must prepay the full year at only $898/yr!

Target Market(s)

business owners

Industry/Entity Type

Marketing

Requirements
Must have
• 768px × 1180px IS THE SIZE vertical

Use this content:

Nice to have
• Use this content:

Should not have
• Use this content:

```html
<!DOCTYPE html>
<html lang="en">
<head>
<meta charset="utf-8">
<title>Annual Upgrade Banner</title>
<link rel="stylesheet" href="https://fonts.googleapis.com/css2?family=Russo+One&family=Ubuntu:wght@500;700&display=swap">
<style>
  :root {
    --stage: #333333;
    --caption: #f2f2f2;
    --red: #c80000;
    --blue-top: #0a5aa0;
    --blue-bottom: #0b3f78;
    --white: #ffffff;
    --ink: #333333;
    --price-blue: #0b4d95;
    --green-top: #52b255;
    --green-bottom: #3c9240;
    --green-shadow: #2a5a2c;
    --panel-fade: #e6e6e6;
  }
  html, body {
    margin: 0;
    padding: 0;
    width: 980px;
    height: 1200px;
    overflow: hidden;
    background: var(--stage);
  }
  .stage {
    position: relative;
    width: 980px;
    height: 1200px;
  }
  .size-caption {
    position: absolute;
    top: 34px;
    left: 0;
    width: 980px;
    text-align: center;
    font-family: "Ubuntu", sans-serif;
    font-weight: 500;
    font-size: 24px;
    color: var(--caption);
    margin: 0;
  }
  .banner {
    position: absolute;
    left: 159px;
    top: 110px;
    width: 665px;
    height: 1021px;
    overflow: hidden;
    background: linear-gradient(to bottom, var(--white) 0%, var(--white) 60%, var(--panel-fade) 100%);
    box-shadow: 0 10px 40px rgba(0,0,0,0.55);
  }
  .headline-band {
    position: absolute;
    left: 0; top: 0;
    width: 665px;
    height: 327px;
    background: var(--red);
  }
  .headline {
    margin: 0;
    font-family: "Russo One", sans-serif;
    font-weight: 400;
    color: var(--white);
    text-align: center;
    text-transform: uppercase;
  }
  .headline span { position: absolute; left: 0; width: 665px; line-height: 1; }
  .headline .lead { font-size: 38px; }
  .headline .l1 { top: 36px; }
  .headline .l2 { top: 79px; }
  .headline .big { font-size: 54px; }
  .headline .l3 { top: 135px; }
  .headline .l4 { top: 192px; }
  .headline .l5 { top: 248px; font-size: 58px; }

  .promise-band { position: absolute; left: 0; top: 327px; width: 665px; height: 190px; }
  .promise {
    position: absolute;
    left: 0; top: 0;
    width: 665px;
    margin: 0;
    font-family: "Russo One", sans-serif;
    color: var(--white);
    text-transform: uppercase;
    text-align: center;
    font-size: 30px;
    line-height: 41px;
    padding-top: 27px;
  }

  .offer {
    position: absolute;
    left: 0; top: 548px;
    width: 665px;
    margin: 0;
    text-align: center;
    font-family: "Russo One", sans-serif;
    font-size: 74px;
    line-height: 1;
    color: var(--red);
  }
  .offer sup { font-size: 38px; vertical-align: 26px; margin-left: 10px; }

  .offer-detail {
    position: absolute;
    left: 0; top: 635px;
    width: 665px;
    margin: 0;
    text-align: center;
    font-family: "Ubuntu", sans-serif;
    font-weight: 500;
    font-size: 31px;
    line-height: 41px;
    letter-spacing: -0.5px;
    color: var(--ink);
  }
  .monthly-price {
    font-family: "Russo One", sans-serif;
    color: var(--price-blue);
    font-size: 30px;
  }
  .monthly-price sup { font-size: 17px; vertical-align: 12px; }

  .cta { position: absolute; left: 45px; top: 749px; width: 576px; height: 166px; }
  .cta svg { position: absolute; left: 0; top: 0; }
  .cta-label {
    position: absolute;
    left: 0; top: 20px;
    width: 576px;
    margin: 0;
    text-align: center;
    font-family: "Russo One", sans-serif;
    font-size: 47px;
    line-height: 54px;
    letter-spacing: -1px;
    color: #f4f4ee;
    text-transform: uppercase;
    text-shadow: 3px 3px 0 var(--green-shadow);
  }

  .terms {
    position: absolute;
    left: 0; top: 952px;
    width: 665px;
    margin: 0;
    text-align: center;
    font-family: "Ubuntu", sans-serif;
    font-weight: 500;
    font-size: 26px;
    letter-spacing: -0.6px;
    color: var(--ink);
  }
  .terms .year-price { color: var(--red); font-weight: 700; }
</style>
</head>
<body>
<div class="stage">
  <p class="size-caption">B2B Marketing Agency Vertical 768px × 1180px IS THE SIZE</p>

  <section class="banner">
    <div class="headline-band">
      <h1 class="headline">
        <span class="lead l1">Are You Ready To</span>
        <span class="lead l2">Commit To Taking</span>
        <span class="big l3">Taking Your</span>
        <span class="big l4">Business To</span>
        <span class="big l5">The Next Level?</span>
      </h1>
    </div>

    <div class="promise-band">
      <svg width="665" height="190" viewBox="0 0 665 190" aria-hidden="true">
        <defs>
          <linearGradient id="promiseFill" x1="0" y1="0" x2="0" y2="1">
            <stop offset="0" stop-color="var(--blue-top)"/>
            <stop offset="1" stop-color="var(--blue-bottom)"/>
          </linearGradient>
        </defs>
        <polygon points="0,0 665,0 665,148 332,190 0,148" fill="url(#promiseFill)"/>
      </svg>
      <p class="promise">Because We're In This&nbsp; For<br>The Long-Haul &amp; Dedicated<br>To Your Success...</p>
    </div>

    <h2 class="offer">Save<sup>$</sup>300</h2>
    <p class="offer-detail">By Upgrading To An Annual<br>Membership &amp; Pay Only <span class="monthly-price"><sup>$</sup>74/mth</span></p>

    <div class="cta">
      <svg width="576" height="166" viewBox="0 0 576 166" aria-hidden="true">
        <defs>
          <linearGradient id="ctaFill" x1="0" y1="0" x2="0" y2="1">
            <stop offset="0" stop-color="var(--green-top)"/>
            <stop offset="1" stop-color="var(--green-bottom)"/>
          </linearGradient>
        </defs>
        <path d="M12 0 H564 Q576 0 576 12 V120 Q576 130 564 132 L288 166 L12 132 Q0 130 0 120 V12 Q0 0 12 0 Z" fill="url(#ctaFill)"/>
      </svg>
      <p class="cta-label">Yes, Upgrade My<br>Plan Right Now!</p>
    </div>

    <p class="terms">*Must prepay the full year at only <span class="year-price">$898/yr!</span></p>
  </section>
</div>
</body>
</html>
```